Harbor Wings is an innovative offering which enables the mass market to book seats on private jets at commercial airline prices to destinations worldwide.

We need a lgog and Wordpress theme header for this initiative. Will like need other matrials but need these two images asap

```html
<!DOCTYPE html>
<html lang="en">
<head>
<meta charset="utf-8">
<title>Harbor Wings</title>
<link rel="stylesheet" href="https://fonts.googleapis.com/css2?family=Arimo:wght@400;700&family=Archivo+Narrow:wght@700&display=swap">
<style>
:root{
  --sky:#3db5d7;
  --sky-light:#6fd0ea;
  --page:#e9e8e2;
  --band:#f4f4ee;
  --rule:#c9c8c2;
  --tab:#cfcec8;
  --panel-top:#3f7f9e;
  --panel-bottom:#2c5f7d;
  --ink:#3c3c3c;
  --text:#222;
  --link:#3aa0c8;
  --red:#c8140b;
  --white:#fff;
}
*{box-sizing:border-box;margin:0;padding:0}
html,body{width:1000px;height:1200px;overflow:hidden}
body{position:relative;background:var(--page);font-family:Arimo,Arial,sans-serif;color:var(--text)}
.abs{position:absolute}
.masthead{left:0;top:0;width:1000px;height:145px;background:linear-gradient(90deg,#46bddd 0%,var(--sky-light) 25%,var(--sky) 55%,#3ab3d5 100%)}
.world-map{left:655px;top:0;width:345px;height:140px;background:radial-gradient(ellipse at 50% 45%,rgba(190,235,248,.55),rgba(190,235,248,0) 70%)}
.brand{left:63px;top:40px;font-weight:700;font-size:50px;letter-spacing:-1px;color:var(--white);line-height:1}
.search{left:748px;top:58px;width:176px;height:22px;border-radius:8px;background:linear-gradient(#b8e6f3,#8fd4ea);font-size:12px;color:#557;padding:4px 0 0 17px}
.search-icon{left:928px;top:56px}
.navband{left:0;top:145px;width:1000px;height:67px;background:var(--band);border-top:3px solid #d8d8d2;border-bottom:4px solid var(--rule)}
.nav a{position:absolute;top:151px;height:43px;display:flex;align-items:center;justify-content:center;background:linear-gradient(#f0f0ea,#dfded8);border:1px solid #cfcec8;font-size:18px;color:var(--ink);text-decoration:none}
.hero{left:50px;top:226px;width:590px;height:295px;border-radius:4px;overflow:hidden;background:linear-gradient(160deg,#33425e 0%,#6a6f86 35%,#d99a4a 55%,#f1c26d 65%,#7a6a7a 100%)}
.hero-dots{right:0;top:0;width:30px;height:295px;background:rgba(70,70,70,.45)}
.hero-dots span{position:absolute;left:8px;width:13px;height:13px;border-radius:50%;background:#3a3a3a;box-shadow:inset 0 1px 2px #777}
.hero-dots span.on{background:#fff}
.welcome{left:50px;top:528px;width:587px;height:310px;border-radius:4px;background:#d2d1cb}
.welcome h1{position:absolute;left:16px;top:10px;font-size:21px;font-variant:small-caps;font-weight:700;color:var(--ink)}
.welcome p{position:absolute;left:16px;width:545px;font-size:12px;line-height:13.7px;color:#111}
.tabs div{position:absolute;top:226px;height:35px;border-radius:4px 4px 0 0;background:var(--tab);font-size:12px;color:#333;display:flex;align-items:center;justify-content:center}
.tabs .active{background:var(--panel-top);color:var(--white);font-weight:700}
.booking{left:644px;top:260px;width:307px;height:349px;border-radius:0 0 4px 4px;background:linear-gradient(var(--panel-top),var(--panel-bottom))}
.booking .lbl{position:absolute;color:var(--white);font-size:13px}
.booking .radio{position:absolute;width:9px;height:9px;border-radius:50%;background:#fff;border:2px solid #fff;box-shadow:inset 0 0 0 2px #fff,inset 0 0 0 5px #222}
.booking .radio.off{box-shadow:none}
.booking .field{position:absolute;height:20px;background:#fff;border:1px solid #333;font-size:12px;color:#999;padding:2px 5px}
.booking .select{position:absolute;height:20px;background:#fff;border:1px solid #555;font-size:12px;color:#999;padding:2px 4px}
.booking .select i{position:absolute;right:0;top:0;width:18px;height:18px;background:#6a8fbd}
.booking .go{position:absolute;left:203px;top:302px;width:78px;height:24px;background:var(--red);color:#fff;font-size:12px;font-weight:700;display:flex;align-items:center;justify-content:center}
.sales{left:644px;top:621px;width:306px;height:216px;border-radius:4px;background:var(--white)}
.sales h2{position:absolute;left:18px;top:10px;font-family:"Archivo Narrow",Arial,sans-serif;font-size:24px;color:var(--ink)}
.sales a{position:absolute;left:8px;width:295px;font-size:12px;line-height:16px;color:var(--link);text-decoration:none;padding-bottom:6px;border-bottom:1px solid #bfd3dc}
.gallery-title{left:64px;top:871px;font-size:20px;font-weight:700;font-variant:small-caps;color:var(--ink)}
.gallery-rule{left:62px;top:896px;width:864px;height:1px;background:#777}
.thumb{width:195px;height:144px;border:3px solid #fff;box-shadow:0 2px 8px rgba(0,0,0,.35)}
.footer{left:0;top:1138px;width:1000px;height:62px;background:var(--band);border-top:3px solid #d8d8d2}
.copyright{left:66px;top:1157px;font-size:12px;color:#333}
.social{top:1150px;width:28px;height:28px;border-radius:5px;background:#8aa9b8}
</style>
</head>
<body>
<header>
  <div class="abs masthead"></div>
  <div class="abs world-map" role="img" aria-label="Faint world map"></div>
  <div class="abs brand">Harbor Wings</div>
  <div class="abs search">Search</div>
  <svg class="abs search-icon" width="38" height="30" viewBox="0 0 38 30"><circle cx="13" cy="12" r="9" fill="#dfe6ea" stroke="#8a969c" stroke-width="3"/><line x1="20" y1="18" x2="35" y2="27" stroke="#7d868b" stroke-width="5" stroke-linecap="round"/></svg>
  <div class="abs navband"></div>
  <nav class="nav">
    <a style="left:51px;width:96px">Home</a>
    <a style="left:149px;width:97px">About us</a>
    <a style="left:248px;width:147px">Charter services</a>
    <a style="left:397px;width:123px">Aircraft Sales</a>
    <a style="left:522px;width:131px">Aircraft Clients</a>
    <a style="left:656px;width:96px">Support</a>
    <a style="left:755px;width:96px">Careers</a>
    <a style="left:854px;width:95px">Contact</a>
  </nav>
</header>

<main>
  <section class="abs hero" role="img" aria-label="Private jet flying above clouds at sunset">
    <div class="abs hero-dots">
      <span class="on" style="top:20px"></span><span style="top:42px"></span><span style="top:64px"></span><span style="top:86px"></span><span style="top:108px"></span><span style="top:130px"></span><span style="top:152px"></span><span style="top:174px"></span>
    </div>
  </section>

  <section class="abs welcome">
    <h1>Welcome To Harbor Wings ......</h1>
    <p style="top:56px">Lorem ipsum dolor sit amet, consectetuer adipiscing elit, sed diam nonummy nibh euismod tinci-dunt ut laoreet dolore magna aliquam erat volutpat. Ut wisi enim ad minim veniam, quis nostrud exerci tation ullamcorper suscipit lobortis nisl ut aliquip ex ea commodo consequat. Duis autem vel eum iriure dolor in hendrerit in vulputate velit esse molestie consequat, vel illum dolore eu feugiat nulla facilisis at vero eros et accumsan et iusto odio dignissim qui blandit praesent luptatum zzril delenit augue duis dolore te feugait nulla facilisi.</p>
    <p style="top:156px">Lorem ipsum dolor sit amet, consectetuer adipiscing elit, sed diam nonummy nibh euismod tinci-dunt ut laoreet dolore magna aliquam erat volutpat. Ut wisi enim ad minim veniam, quis nostrud exerci tation ullamcorper suscipit lobortis nisl ut aliquip ex ea commodo consequat. Duis autem vel eum iriure dolor in hendrerit in vulputate velit esse molestie consequat, vel illum dolore eu feugiat nulla facilisis at vero eros et accumsan et iusto odio dignissim qui blandit praesent luptatum zzril delenit augue duis dolore te feugait nulla facilisi.</p>
  </section>

  <div class="tabs">
    <div class="active" style="left:644px;width:75px">Flight</div>
    <div style="left:721px;width:75px">International</div>
    <div style="left:798px;width:75px">Hotels</div>
    <div style="left:875px;width:76px">Timetable</div>
  </div>

  <form class="abs booking">
    <span class="radio" style="left:21px;top:32px"></span><span class="lbl" style="left:33px;top:30px;font-size:12px">Round trip</span>
    <span class="radio off" style="left:107px;top:32px"></span><span class="lbl" style="left:119px;top:30px;font-size:12px">One way</span>
    <span class="lbl" style="left:26px;top:58px">From</span><span class="field" style="left:73px;top:56px;width:198px"></span>
    <span class="lbl" style="left:26px;top:86px">To</span><span class="field" style="left:73px;top:84px;width:198px"></span>
    <span class="lbl" style="left:29px;top:123px">Departure Date and Time :</span>
    <span class="field" style="left:28px;top:143px;width:99px">mm/dd/yyy</span>
    <span class="select" style="left:131px;top:143px;width:83px">12:00am<i></i></span>
    <span class="lbl" style="left:29px;top:169px">Return Date and Time :</span>
    <span class="field" style="left:28px;top:186px;width:99px">mm/dd/yyy</span>
    <span class="select" style="left:131px;top:186px;width:83px">12:00am<i></i></span>
    <span class="radio" style="left:21px;top:225px"></span><span class="lbl" style="left:33px;top:222px">Economy Class</span>
    <span class="radio off" style="left:148px;top:225px"></span><span class="lbl" style="left:161px;top:222px">Business Class</span>
    <span class="lbl" style="left:31px;top:249px">Passengers :</span>
    <span class="field" style="left:28px;top:268px;width:115px;color:#777">#&nbsp;of Passengers</span>
    <span class="go">SEARCH</span>
  </form>

  <aside class="abs sales">
    <h2>Aircraft Sales :</h2>
    <a style="top:64px">The global magazine for everyone in business aviation. View private jets &amp; business aircraft for sale this month:</a>
    <a style="top:106px">The global magazine for everyone in business aviation. View private jets &amp; business aircraft for sale this month:</a>
    <a style="top:147px">The global magazine for everyone in business aviation. View private jets &amp; business aircraft for sale this month:</a>
  </aside>

  <h2 class="abs gallery-title">Aircraft Gallery ....</h2>
  <div class="abs gallery-rule"></div>
  <div class="abs thumb" style="left:71px;top:936px;background:linear-gradient(#5d7387 0%,#aab3b9 45%,#6f7a63 70%,#4a4e4b 100%)" role="img" aria-label="White business jet parked on the apron"></div>
  <div class="abs thumb" style="left:286px;top:935px;background:linear-gradient(#3f6fae 0%,#8aa8cf 45%,#e7ecf1 75%,#c6ced8 100%)" role="img" aria-label="Light jet flying above clouds"></div>
  <div class="abs thumb" style="left:504px;top:935px;background:linear-gradient(#6b6a66 0%,#3d3c3a 40%,#2a2a2a 100%)" role="img" aria-label="Jet parked inside a hangar"></div>
  <div class="abs thumb" style="left:724px;top:935px;background:linear-gradient(#6b8a55 0%,#4f7a3a 55%,#3f6530 100%)" role="img" aria-label="Small jet flying over green fields"></div>
</main>

<footer>
  <div class="abs footer"></div>
  <p class="abs copyright">Copyright 2010 &copy; Harbor Wings . All Rights Reserved</p>
  <span class="abs social" style="left:836px"></span>
  <span class="abs social" style="left:876px"></span>
  <span class="abs social" style="left:916px"></span>
</footer>
</body>
</html>
```